Designing promotion page - poster for Folk High School

I would like a attractive and well-designed page /poster used in a catalogue for the Tavelund Learning Colleges.
The dimensions on the graphical element:
Width: 180 mm
Hight:186 mm
Resolution: min. 450 dpi
This graphical element will be combined with other information about the school, that is static and we cannot change. Please see attachment (“Folk High School – placement of graphic”). The almost square area in the middle of the page iss the one that the designed grapichal element will fill.
A part of completing this, is to hand over the workfile to us in the end when we choose the design (Adobe Photoshop PSD or an InDesign INDD file must be used)
There are also attached some pictures that you are free to use in creating the design as you like. You will choose how many pictures you want to use. Please cut, scale, adjust and sharpen them as you like. Only one requirement: Please use one of the Sri Lanka pictures.
Be creative.
The following text-elements must be used in the page (They are also prioritized – number one means: most important that the reader reads…)
1. Møtet som forandrer --- headline. Yep; needs a font supporting ÆØÅ...
2. Multisport --- different courses we provide at our school.
- Data Media – Japan
- Barn i Fokus
- Helse og Velvære
- Globalt Fokus – Afrika
- Fotball
- Bil og Motor
- Internasjonal
- Worship – Australia
- KISS-friluft
- Høy Puls
Alle linjer reiser på egne turer i inn –og utland! ---- This should be included as the different courses, but in the bottum of the «box».
3. Spennende fellestur for alle til Sri Lanka ---- Use together with the picture from Sri Lanke (Not too large picture!)
4. Hva skal du bli? ---- small headline.
Vi er gode på veiledning, og hjelper deg med å finne ut hva du skal bli.
5. Flott skole:
- Basseng
- Styrkerom
- Gymsal
- Internatstuer
- Filmsal
- Skolekjøkken
- Verksted
- Fotostudio
- Fitnessrom
_________
The students attending our school is between 18-20 years. Of course, the design and expression must meet their expectations.
Looking forward to see the first drafts!
To understand what this should look like: Check the following link:
https://leafrack.net/tavelundskolen/docs/tlc_guide__18__web
The poster / graphic we want to create, is similar to the one you find in this brochure from page 20.

```html
<!DOCTYPE html>
<html lang="no">
<head>
<meta charset="utf-8">
<title>Møtet som forandrer – Tavelund Learning Colleges</title>
<link rel="stylesheet" href="https://fonts.googleapis.com/css2?family=Montserrat:wght@300;400;500;700;800&display=swap">
<style>
  :root {
    --blue-deep: #0a2a8c;
    --blue-mid: #1140b4;
    --blue-bright: #1a4fd0;
    --white: #ffffff;
    --ink: #111111;
    --night: #0c1a4a;
  }
  * { margin: 0; padding: 0; box-sizing: border-box; }
  html, body { width: 1161px; height: 1200px; overflow: hidden; background: var(--white); }
  body { font-family: "Montserrat", Arial, sans-serif; color: var(--white); }
  .poster { position: relative; width: 1161px; height: 1200px; background: var(--white); }

  .headline-band {
    position: absolute; left: 0; top: 0; width: 1161px; height: 137px;
    background: linear-gradient(90deg, var(--blue-deep) 0%, var(--blue-mid) 45%, var(--blue-bright) 75%, var(--blue-deep) 100%);
    display: flex; align-items: center; justify-content: center;
  }
  .headline { font-size: 70px; letter-spacing: -0.5px; font-weight: 300; line-height: 1; }
  .headline strong { font-weight: 700; }

  .course-panel {
    position: absolute; left: 0; top: 161px; width: 485px; height: 600px;
    background: radial-gradient(ellipse at 50% 40%, var(--blue-bright) 0%, var(--blue-mid) 45%, var(--blue-deep) 100%);
  }
  .course-title {
    position: absolute; top: 10px; left: 0; width: 100%; text-align: center;
    font-size: 60px; font-weight: 700; letter-spacing: -0.5px;
  }
  .course-divider {
    position: absolute; left: 248px; top: 90px; width: 3px; height: 428px; background: var(--white);
  }
  .course-grid {
    position: absolute; left: 0; top: 90px; width: 485px; height: 428px;
    display: grid; grid-template-columns: 227px 213px; column-gap: 45px;
    grid-template-rows: repeat(5, 1fr); align-items: center;
    font-size: 28px; line-height: 32px; font-weight: 400;
  }
  .course-left { text-align: right; }
  .course-right { text-align: left; }
  .course-note {
    position: absolute; left: 28px; top: 527px; width: 440px;
    font-size: 23px; line-height: 31px; font-weight: 400;
  }

  .photo { position: absolute; }
  .photo-sunset {
    left: 512px; top: 161px; width: 649px; height: 600px;
    background: linear-gradient(180deg, #2b3f63 0%, #5d7aa2 28%, #a08a7a 55%, #e08a3a 62%, #3e4a2a 72%, #2a3a1c 100%);
  }
  .photo-beach {
    left: 0; top: 785px; width: 276px; height: 415px;
    background: linear-gradient(180deg, #5e9fd8 0%, #b9d6ee 35%, #4b8f9a 55%, #d9c39b 68%, #e6d2ad 100%);
  }
  .beach-caption {
    position: absolute; left: 19px; top: 1124px; width: 240px;
    font-size: 17px; line-height: 31px; color: var(--ink); font-weight: 400;
  }

  .guidance-panel {
    position: absolute; left: 306px; top: 785px; width: 855px; height: 415px;
    background: linear-gradient(180deg, #0f2470 0%, var(--night) 55%, #1a1830 80%, #3a2418 100%);
  }
  .guidance-title {
    position: absolute; left: 331px; top: 828px; font-size: 48px; font-weight: 700; letter-spacing: -0.3px;
  }
  .guidance-text {
    position: absolute; left: 331px; top: 893px; width: 460px;
    font-size: 23.5px; line-height: 31px; font-weight: 400;
  }
  .facilities {
    position: absolute; left: 803px; top: 824px; width: 350px;
    font-size: 26px; line-height: 34px; font-weight: 400;
  }
  .facilities strong { font-weight: 700; }
</style>
</head>
<body>
<main class="poster">
  <header class="headline-band">
    <h1 class="headline"><strong>Møtet</strong> som <strong>forandrer</strong></h1>
  </header>

  <section class="course-panel">
    <h2 class="course-title">Multisport</h2>
    <div class="course-divider"></div>
    <div class="course-grid">
      <div class="course-left">Data Media<br>Japan</div>
      <div class="course-right">Barn i Fokus</div>
      <div class="course-left">Helse og<br>Velvære</div>
      <div class="course-right">Globalt<br>Fokus&nbsp; Afrika</div>
      <div class="course-left">Fotball</div>
      <div class="course-right">Bil og Motor</div>
      <div class="course-left">Internasjonal</div>
      <div class="course-right">Worship<br>Australia</div>
      <div class="course-left">KISS-friluft</div>
      <div class="course-right">Høy Puls</div>
    </div>
    <p class="course-note">Alle linjer reiser på egne turer i inn-og utland!</p>
  </section>

  <div class="photo photo-sunset" role="img" aria-label="Fire students standing in a grassy savanna, watching the sunset under a cloudy sky"></div>

  <div class="photo photo-beach" role="img" aria-label="Sandy beach in Sri Lanka with palm trees, seagulls and two people walking by the sea"></div>
  <p class="beach-caption">Spennende fellestur for alle til Sri Lanka.</p>

  <section class="guidance-panel" role="img" aria-label="Students gathered around a campfire at dusk by the water, one playing guitar"></section>
  <h2 class="guidance-title">Hva Skal Du Bli?</h2>
  <p class="guidance-text">Vi er gode på veiledning, og hjelper deg med å finne ut hva du skal bli.</p>
  <p class="facilities"><strong>Flott skole:</strong> Basseng<br>Styrkerom Gymsal<br>Internatstuer • Filmsal<br>Skolekjøkken • Verksted<br>Fotostudio • Fitnessrom</p>
</main>
</body>
</html>
```